KV HOLDING Business Cards

I need business cards for "KV Holding group LLC" doublesided... logo on the back (also include logo on front)
logo attached to project... i have jpg up..
Company Info:
418 East Marlow Avenue, Suite 7B
Chicago, Illinois 60617
facsimile 312-555-0188 (list fax, address, website on all cards.)
www.kvholdinggroup.example
Three different people on cards:
Dorian P. Kell, CPA MST
Principal
ofc 312-555-0142
mobile 312-555-0167
dorianpkell@kvholdinggroup.example
Marcus T. Brenholt, CPA MST
Principal
marcustbrenholt@kvholdinggroup.example
mobile 708-555-0119
ofc 312-555-0142
Nigel F Carrow
Principal
ofc 312-555-0142
no mobile
nigelfcarrow@kvholdinggroup.example
I have multiple projects listed.. see below:
Business cards for amber gate equity llc
letterhead
envelopes
Business cards for KV Holding LLC
letterhead
envelopes
Target Market(s)
rich people
Industry/Entity Type
Business
Look and feel

```html
<!DOCTYPE html>
<html lang="en">
<head>
<meta charset="utf-8">
<title>KV Holding Group – Business Cards</title>
<link rel="stylesheet" href="https://fonts.googleapis.com/css2?family=Arimo:wght@400;700&display=swap">
<style>
  :root {
    --navy: #1d4384;
    --ink: #1f3d78;
    --text: #1b2f5c;
    --paper: #ffffff;
    --swoosh: #b9bcc2;
    --stage: #1a1a1a;
  }
  * { box-sizing: border-box; margin: 0; padding: 0; }
  html, body {
    width: 1200px;
    height: 1068px;
    overflow: hidden;
    background: var(--stage);
    font-family: "Arimo", Arial, sans-serif;
  }
  .card-sheet {
    position: relative;
    width: 1200px;
    height: 1068px;
  }
  .card {
    position: absolute;
    top: 370px;
    width: 560px;
    height: 329px;
    background: var(--paper);
    overflow: hidden;
  }
  .card--front { left: 30px; }
  .card--back  { left: 610px; }

  .card__art {
    position: absolute;
    inset: 0;
    width: 560px;
    height: 329px;
  }

  /* front */
  .brand {
    position: absolute;
    top: 138px;
    left: 0;
    width: 100%;
    display: flex;
    align-items: center;
    justify-content: center;
    gap: 12px;
  }
  .brand__dot {
    width: 14px;
    height: 14px;
    border-radius: 50%;
    background: var(--ink);
  }
  .brand__name {
    font-size: 28px;
    font-weight: 400;
    color: var(--ink);
    letter-spacing: 0.5px;
  }
  .address {
    position: absolute;
    top: 192px;
    width: 100%;
    text-align: center;
    font-size: 17px;
    font-weight: 700;
    line-height: 23px;
    color: var(--text);
  }
  .band-line {
    position: absolute;
    top: 278px;
    display: flex;
    align-items: center;
    gap: 10px;
    font-size: 17px;
    font-weight: 700;
    color: #fff;
  }
  .band-line--fax { left: 38px; }
  .band-line--web { right: 36px; }
  .icon { width: 20px; height: 20px; fill: currentColor; }

  /* back */
  .office {
    position: absolute;
    top: 16px;
    width: 100%;
    display: flex;
    justify-content: center;
    align-items: center;
    gap: 4px;
    font-size: 16px;
    font-weight: 700;
    color: var(--ink);
  }
  .office .icon { width: 17px; height: 17px; }
  .person {
    position: absolute;
    width: 100%;
    text-align: center;
    font-size: 17px;
    line-height: 24px;
    color: var(--text);
  }
  .person__name { font-weight: 700; }
  .person--one   { top: 56px; }
  .person--two   { top: 154px; }
  .person--three { top: 248px; }
</style>
</head>
<body>
<main class="card-sheet">

  <section class="card card--front" aria-label="Card front">
    <svg class="card__art" viewBox="0 0 560 329" aria-hidden="true">
      <defs>
        <linearGradient id="frontSwoosh" x1="0" x2="1" y1="0" y2="0">
          <stop offset="0" stop-color="#9fa3aa"/>
          <stop offset="0.6" stop-color="#d5d7db"/>
          <stop offset="1" stop-color="#eef0f2"/>
        </linearGradient>
      </defs>
      <path d="M0,232 C140,220 300,252 560,222 L560,240 C300,266 140,236 0,246 Z" fill="url(#frontSwoosh)"/>
      <path d="M0,246 C140,236 300,266 560,240 L560,329 L0,329 Z" fill="var(--navy)"/>
    </svg>

    <div class="brand">
      <span class="brand__dot"></span>
      <span class="brand__name">KV Holding Group LLC</span>
    </div>

    <p class="address">418 East Marlow Avenue, Suite 7B<br>Chicago, Illinois 60617</p>

    <p class="band-line band-line--fax">
      <svg class="icon" viewBox="0 0 20 20" aria-hidden="true">
        <rect x="1" y="7" width="4" height="11" rx="1"/>
        <rect x="6" y="6" width="13" height="12" rx="1"/>
        <rect x="8" y="2" width="9" height="5" fill="#fff"/>
        <rect x="8.8" y="2.8" width="7.4" height="3.4"/>
        <rect x="8" y="9" width="9" height="2.5" fill="#1d4384"/>
        <rect x="8" y="13" width="2" height="2" fill="#1d4384"/>
        <rect x="11.5" y="13" width="2" height="2" fill="#1d4384"/>
        <rect x="15" y="13" width="2" height="2" fill="#1d4384"/>
      </svg>
      312-555-0188
    </p>
    <p class="band-line band-line--web">www.kvholdinggroup.example</p>
  </section>

  <section class="card card--back" aria-label="Card back">
    <svg class="card__art" viewBox="0 0 560 329" aria-hidden="true">
      <defs>
        <linearGradient id="backSwoosh" x1="0" x2="1" y1="0" y2="0">
          <stop offset="0" stop-color="#9a9ea5"/>
          <stop offset="0.55" stop-color="#c9ccd1"/>
          <stop offset="1" stop-color="#eceef0"/>
        </linearGradient>
      </defs>
      <path d="M0,132 C160,124 330,146 560,140 L560,146 C330,152 160,136 0,142 Z" fill="url(#backSwoosh)"/>
      <path d="M0,230 C160,222 330,244 560,238 L560,243 C330,250 160,234 0,240 Z" fill="url(#backSwoosh)"/>
    </svg>

    <p class="office">
      Office
      <svg class="icon" viewBox="0 0 20 20" aria-hidden="true">
        <path d="M5.2 2.2l2.4 3.4c.3.5.2 1.1-.2 1.5L6.2 8.3c1 2.2 2.8 4 5 5l1.2-1.2c.4-.4 1-.5 1.5-.2l3.4 2.4c.5.4.6 1 .3 1.5l-1.2 1.8c-.5.7-1.4 1-2.2.8C8.6 17 3 11.4 1.6 5.8c-.2-.8.1-1.7.8-2.2L4.2 2.4c.3-.3.7-.3 1 -.2z"/>
      </svg>
      312-555-0142
    </p>

    <div class="person person--one">
      <p><span class="person__name">Dorian P. Kell</span>, CPA MST, Principal</p>
      <p>mobile 312-555-0167</p>
      <p>dorianpkell@kvholdinggroup.example</p>
    </div>

    <div class="person person--two">
      <p><span class="person__name">Marcus T. Brenholt</span>, CPA MST, Principal</p>
      <p>marcustbrenholt@kvholdinggroup.example</p>
      <p>mobile 708-555-0119</p>
    </div>

    <div class="person person--three">
      <p><span class="person__name">Nigel F Carrow</span>, Principal</p>
      <p>nigelfcarrow@kvholdinggroup.example</p>
    </div>
  </section>

</main>
</body>
</html>
```